Amber Hollow Productions

I need a business card design for a new freelance film production company using or incorporating the logo:
I want the card to be creative, minimal, yet professional. Feel free to use a variety of different shapes and sizes/ textures for the card.

Industry/Entity Type

Film Production

```html
<!DOCTYPE html>
<html lang="en">
<head>
<meta charset="utf-8">
<title>Amber Hollow Productions — Business Card</title>
<link href="https://fonts.googleapis.com/css2?family=Jost:wght@300;400;500&display=swap" rel="stylesheet">
<style>
  :root {
    --brand-blue: #2d60aa;
    --brand-mist: #c8d5e8;
    --card-paper: #f9f9f9;
    --card-edge: #e2e2e2;
    --page-bg: #ffffff;
    --stage-bg: #eef1f5;
  }
  * { margin: 0; padding: 0; box-sizing: border-box; }
  html, body { width: 900px; height: 1200px; overflow: hidden; }
  body {
    position: relative;
    background: var(--page-bg);
    font-family: "Jost", "Futura", sans-serif;
    color: var(--brand-blue);
  }

  .brand-lockup {
    position: absolute; left: 0; top: 96px; width: 900px;
    text-align: center; line-height: 1;
  }
  .brand-lockup .wordmark { font-size: 29px; font-weight: 400; letter-spacing: 0.5px; }
  .brand-lockup .tagline { font-size: 9px; letter-spacing: 5px; margin-top: 6px; }

  .card {
    position: absolute; width: 221px; height: 381px; top: 256px;
    background: var(--card-paper); border: 3px solid var(--card-edge);
    border-radius: 4px; overflow: hidden;
  }
  .card--front { left: 198px; }
  .card--back { left: 495px; }

  .card-band { position: absolute; left: 0; right: 0; bottom: 0; height: 90px; }
  .card--front .card-band { background: var(--brand-mist); }
  .card--back .card-band { background: var(--brand-blue); }

  .front-lockup { position: absolute; top: 124px; width: 100%; text-align: center; line-height: 1; }
  .front-lockup .wordmark { font-size: 17px; }
  .front-lockup .tagline { font-size: 6px; letter-spacing: 3px; margin-top: 4px; }

  .name-dot {
    position: absolute; left: -18px; top: 52px; width: 68px; height: 68px;
    border-radius: 50%; background: var(--brand-blue);
  }
  .contact { position: absolute; left: 54px; top: 80px; line-height: 1; white-space: nowrap; }
  .contact .person { font-size: 21px; font-weight: 400; font-variant: small-caps; letter-spacing: 0.5px; }
  .contact .role { font-size: 12px; font-variant: small-caps; margin-top: 2px; }
  .contact .email, .contact .phone { color: var(--brand-mist); }
  .contact .email { font-size: 10px; margin-top: 5px; }
  .contact .phone { font-size: 14px; letter-spacing: 0.5px; margin-top: 3px; }

  .repeat-column {
    position: absolute; top: 10px; height: 255px;
    writing-mode: vertical-rl; transform: rotate(180deg);
    display: flex; justify-content: space-around;
    color: var(--brand-mist); font-size: 10px; line-height: 1; white-space: nowrap;
  }
  .repeat-column--a { left: 186px; }
  .repeat-column--b { left: 201px; }

  .view-label {
    position: absolute; top: 648px; font-size: 22px; font-weight: 300;
    font-variant: small-caps; color: var(--brand-mist); letter-spacing: 0.5px;
  }
  .view-label--front { left: 274px; }
  .view-label--back { left: 574px; }

  .swatch { position: absolute; top: 599px; width: 73px; height: 73px; }
  .swatch--blue { left: 40px; background: var(--brand-blue); }
  .swatch--mist { left: 788px; background: var(--brand-mist); }
  .swatch-code {
    position: absolute; top: 676px; font-size: 21px; font-weight: 300;
    font-variant: small-caps; letter-spacing: 0.5px;
  }
  .swatch-code--blue { left: 40px; color: var(--brand-blue); }
  .swatch-code--mist { left: 788px; color: var(--brand-mist); }

  .stage {
    position: absolute; left: 147px; top: 712px; width: 606px; height: 455px;
    background: var(--stage-bg);
  }
  .stage .landscape {
    position: absolute; left: 40px; top: 150px; width: 270px; height: 160px;
    background: var(--card-paper); border: 2px solid var(--card-edge); overflow: hidden;
  }
  .landscape .card-band { top: 0; bottom: 0; left: 0; right: auto; width: 70px; height: auto; background: var(--brand-blue); }
  .landscape .name-dot { left: 150px; top: -18px; width: 56px; height: 56px; }
  .landscape .contact { left: 120px; top: 48px; }
  .landscape .contact .person { font-size: 17px; }
  .landscape .contact .role { font-size: 10px; }
  .landscape .contact .email { font-size: 9px; }
  .landscape .contact .phone { font-size: 12px; }
  .landscape .repeat-row {
    position: absolute; left: 80px; bottom: 10px; font-size: 8px;
    color: var(--brand-mist); white-space: nowrap; word-spacing: 2px;
  }
  .stage .portrait {
    position: absolute; left: 370px; top: 70px; width: 180px; height: 300px;
    background: var(--card-paper); border: 2px solid var(--card-edge); overflow: hidden;
  }
  .portrait .front-lockup { top: 60px; }
  .portrait .card-band { height: 80px; background: var(--brand-mist); }
</style>
</head>
<body>
  <header class="brand-lockup">
    <div class="wordmark">AMBER HOLLOW</div>
    <div class="tagline">PRODUCTIONS</div>
  </header>

  <section class="card card--front" aria-label="Card front">
    <div class="front-lockup">
      <div class="wordmark">AMBER HOLLOW</div>
      <div class="tagline">PRODUCTIONS</div>
    </div>
    <div class="card-band"></div>
  </section>

  <section class="card card--back" aria-label="Card back">
    <div class="name-dot"></div>
    <div class="contact">
      <div class="person">Rowan Pike</div>
      <div class="role">Account Manager</div>
      <div class="email">rpike@amberhollow.com</div>
      <div class="phone">555.014.2730</div>
    </div>
    <div class="repeat-column repeat-column--a">
      <span>AMBER HOLLOW</span><span>AMBER HOLLOW</span><span>AMBER HOLLOW</span>
    </div>
    <div class="repeat-column repeat-column--b">
      <span>AMBER HOLLOW</span><span>AMBER HOLLOW</span><span>AMBER HOLLOW</span>
    </div>
    <div class="card-band"></div>
  </section>

  <div class="view-label view-label--front">Front</div>
  <div class="view-label view-label--back">Back</div>

  <div class="swatch swatch--blue"></div>
  <div class="swatch-code swatch-code--blue">2d60aa</div>
  <div class="swatch swatch--mist"></div>
  <div class="swatch-code swatch-code--mist">c8d5e8</div>

  <section class="stage" aria-label="Cards laid out flat">
    <div class="landscape">
      <div class="card-band"></div>
      <div class="name-dot"></div>
      <div class="contact">
        <div class="person">Rowan Pike</div>
        <div class="role">Account Manager</div>
        <div class="email">rpike@amberhollow.com</div>
        <div class="phone">555.014.2730</div>
      </div>
      <div class="repeat-row">AMBER HOLLOW · AMBER HOLLOW · AMBER HOLLOW</div>
    </div>
    <div class="portrait">
      <div class="front-lockup">
        <div class="wordmark">AMBER HOLLOW</div>
        <div class="tagline">PRODUCTIONS</div>
      </div>
      <div class="card-band"></div>
    </div>
  </section>
</body>
</html>
```